Aircraft maintenance buisness card

I am an aircraft mechanic looking for a personal buisness card . I would like my name and a title of Aircraft Maintenance Manager . I would like a suttle picture of an aircraft and helicopter .

elegant and professional wtih my contact .

My name should be on the car and Aircraft Maintenance Manager under with my contact infor below .

i have attached some pictures but i am open to other pics and ideas . I would like a airliner or private jet and a helicopter in the picture . The Images should be suttle and not the main idea . I also uploaded a picture of a jet engine which is cool . Be creative and i will work with you to finalize something .
Updates

Project Deadline Extended
Reason: Looking for more variations . Very good so far but looiking for a bit more styles and i uploaded my logo that i purchased . Please use my logo and be creative with it . I like some variations of black card with maybe some pictures that i uploaded but i am open to ideas . Be creative and i will work with you .

Project Deadline Extended
Reason: Looking for more designs and variations . Not yet satisfied with the designs i have gotten .

Industry/Entity Type

Aviation

Contact Information for Business Card

Aircraft Maintenance Manager

Font styles to use
Serif

Colors

Designer to choose colors to be used in the design.

Requirements
Must have
• An aviation related Logo if possible incorporated in the card possibly
• My name
• Tiberio Malvade Furtunato
• 482 Pellow St.
• Kearny , NJ
• 08519
• Email: Lwskyfixtech@mailvora.com
Nice to have
• Suttle Backround of a Private Jet or Airliner and a Helicopter .

```html
<!DOCTYPE html>
<html lang="en">
<head>
<meta charset="UTF-8">
<title>Dorian K. Halvey – Business Card</title>
<link rel="stylesheet" href="https://fonts.googleapis.com/css2?family=Cinzel:wght@400;600&family=Jost:wght@400;600&display=swap">
<style>
  :root {
    --stage: #1c1c1c;
    --card: #262626;
    --card-edge: #2e2e2e;
    --emboss-dark: #151515;
    --emboss-light: #4a4a4a;
    --ink: #ffffff;
    --ink-muted: #8c8c8c;
    --icon-fill: #e9e9e9;
    --icon-glyph: #262626;
  }
  * { margin: 0; padding: 0; box-sizing: border-box; }
  html, body {
    width: 1200px;
    height: 1000px;
    overflow: hidden;
    background: var(--stage);
  }
  .canvas {
    position: relative;
    width: 1200px;
    height: 1000px;
  }
  .card {
    position: absolute;
    left: 250px;
    width: 700px;
    height: 400px;
    background: var(--card);
    border: 1px solid var(--card-edge);
    box-shadow: 0 14px 30px rgba(0,0,0,0.55);
    display: flex;
    flex-direction: column;
    align-items: center;
  }
  .card--front { top: 60px; justify-content: center; }
  .card--back { top: 540px; padding-top: 92px; }

  /* Front: embossed serif name */
  .front-name {
    font-family: "Cinzel", serif;
    font-weight: 600;
    font-size: 40px;
    letter-spacing: 3px;
    color: var(--emboss-dark);
    text-shadow: 1px 1px 0 var(--emboss-light), -1px -1px 0 #0c0c0c;
  }
  .front-title {
    font-family: "Cinzel", serif;
    font-size: 17px;
    letter-spacing: 2px;
    color: var(--emboss-dark);
    text-shadow: 1px 1px 0 var(--emboss-light);
    margin-top: -4px;
  }

  /* Back: contact side */
  .back-name {
    font-family: "Jost", sans-serif;
    font-weight: 600;
    font-size: 38px;
    letter-spacing: 2px;
    color: var(--ink);
    line-height: 1;
  }
  .back-title {
    font-family: "Jost", sans-serif;
    font-size: 18px;
    letter-spacing: 2px;
    color: var(--ink-muted);
    margin-top: 2px;
  }
  .contact-icons {
    display: flex;
    gap: 6px;
    margin-top: 30px;
  }
  .contact-icons svg { width: 22px; height: 22px; }
  .contact-list {
    list-style: none;
    text-align: center;
    margin-top: 16px;
    font-family: "Jost", sans-serif;
    font-size: 17px;
    letter-spacing: 2px;
    color: var(--ink);
    line-height: 1.4;
  }
  .contact-list .address { margin-top: 4px; }
</style>
</head>
<body>
<main class="canvas">
  <section class="card card--front" aria-label="Card front">
    <h1 class="front-name">DORIAN K. HALVEY</h1>
    <p class="front-title">AIRCRAFT MAINTENANCE MANAGER</p>
  </section>

  <section class="card card--back" aria-label="Card back">
    <h2 class="back-name">DORIAN K. HALVEY</h2>
    <p class="back-title">Aircraft Maintenance Manager</p>

    <div class="contact-icons">
      <svg viewBox="0 0 22 22" aria-label="Phone">
        <circle cx="11" cy="11" r="11" fill="var(--icon-fill)"/>
        <path d="M8 5.5l2 2.5-1.2 1.3c.6 1.5 1.8 2.7 3.4 3.4l1.3-1.2 2.5 2-1.3 2c-4.2-.3-8-4.1-8.4-8.4z" fill="var(--icon-glyph)"/>
      </svg>
      <svg viewBox="0 0 22 22" aria-label="Email">
        <circle cx="11" cy="11" r="11" fill="var(--icon-fill)"/>
        <rect x="5.5" y="7" width="11" height="8" fill="none" stroke="var(--icon-glyph)" stroke-width="1.3"/>
        <path d="M5.5 7l5.5 4.5L16.5 7" fill="none" stroke="var(--icon-glyph)" stroke-width="1.3"/>
      </svg>
      <svg viewBox="0 0 22 22" aria-label="Website">
        <circle cx="11" cy="11" r="11" fill="var(--icon-fill)"/>
        <g fill="none" stroke="var(--icon-glyph)" stroke-width="1.1">
          <circle cx="11" cy="11" r="6"/>
          <ellipse cx="11" cy="11" rx="2.6" ry="6"/>
          <path d="M5 11h12M6 8h10M6 14h10"/>
        </g>
      </svg>
    </div>

    <ul class="contact-list">
      <li>(000) 111 2223</li>
      <li>urname@email.com</li>
      <li>www.ursitename.com</li>
      <li class="address">Your Street Address, Callowmere, OK 125703</li>
    </ul>
  </section>
</main>
</body>
</html>
```